Stonebay Towing Business Card

Towing
Accident towing
Mechanical breakdown
Insurance, salvage and recovery
4wd off road towing
Light & Heavy towing
8347 2516
24 hour business 7 days

Logo can be whole size on front

Industry/Entity Type

Towing/ transport

Contact Information for Business Card

The above

```html
<!DOCTYPE html>
<html lang="en">
<head>
<meta charset="UTF-8">
<title>Stonebay Towing Business Card</title>
<link href="https://fonts.googleapis.com/css2?family=Exo+2:ital,wght@1,800;1,900&family=Montserrat:wght@500;800&display=swap" rel="stylesheet">
<style>
  :root {
    --backdrop: #000000;
    --card: #ffffff;
    --brand-red: #d42027;
    --brand-red-deep: #c01c22;
    --ink: #111111;
  }
  * { margin: 0; padding: 0; box-sizing: border-box; }
  html, body {
    width: 1200px;
    height: 1200px;
    overflow: hidden;
    background: var(--backdrop);
  }
  .canvas {
    position: relative;
    width: 1200px;
    height: 1200px;
    background: var(--backdrop);
  }
  .card {
    position: absolute;
    left: 222px;
    width: 756px;
    height: 432px;
    background: var(--card);
    overflow: hidden;
  }
  .card--front { top: 135px; }
  .card--back { top: 632px; }

  .wordmark {
    font-family: "Montserrat", sans-serif;
    font-weight: 800;
    color: var(--brand-red);
    white-space: nowrap;
  }
  .card--front .wordmark {
    position: absolute;
    left: 0;
    right: 0;
    top: 176px;
    text-align: center;
    font-size: 68px;
    line-height: 80px;
  }
  .card--back .wordmark {
    position: absolute;
    left: 46px;
    top: 52px;
    font-size: 29px;
    line-height: 40px;
  }

  .contact {
    position: absolute;
    right: 40px;
    top: 46px;
    text-align: right;
    font-family: "Exo 2", sans-serif;
    font-style: italic;
    white-space: nowrap;
  }
  .contact__phone {
    display: block;
    font-weight: 900;
    font-size: 47px;
    line-height: 52px;
    letter-spacing: 5px;
    word-spacing: 12px;
    color: var(--brand-red);
  }
  .contact__hours {
    display: block;
    margin-right: 8px;
    font-weight: 800;
    font-size: 18px;
    line-height: 26px;
    letter-spacing: 3.6px;
    word-spacing: 3px;
    color: var(--ink);
    text-transform: uppercase;
  }

  .services {
    position: absolute;
    list-style: none;
    font-family: "Montserrat", sans-serif;
    font-weight: 500;
    font-size: 18px;
    line-height: 32px;
    letter-spacing: 1.2px;
    color: var(--ink);
    white-space: nowrap;
  }
  .services--left {
    right: 482px;
    top: 190px;
    text-align: right;
  }
  .services--right {
    left: 310px;
    top: 152px;
  }

  .accent-band {
    position: absolute;
    left: 0;
    right: 0;
    top: 300px;
    bottom: 0;
    background: linear-gradient(180deg, var(--brand-red) 0%, var(--brand-red-deep) 100%);
  }
</style>
</head>
<body>
<main class="canvas">

  <section class="card card--front">
    <div class="wordmark">Stonebay Towing</div>
  </section>

  <section class="card card--back">
    <div class="accent-band" role="img" aria-label="Decorative red sweeping band across the bottom of the card"></div>

    <div class="wordmark">Stonebay Towing</div>

    <div class="contact">
      <span class="contact__phone">8347 2516</span>
      <span class="contact__hours">24 hour business 7 days</span>
    </div>

    <ul class="services services--left">
      <li>Towing</li>
      <li>Accident towing</li>
      <li>Mechanical breakdown</li>
    </ul>

    <ul class="services services--right">
      <li>Insurance, salvage and recovery</li>
      <li>4wd off road towing</li>
      <li>Light &amp; Heavy towing</li>
    </ul>
  </section>

</main>
</body>
</html>
```